Criação de Papelaria (6 itens) para Beleza
" Somos uma Distribuidora de Cosméticos. Compramos os produtos diretamente das Indústrias e depois revendemos para lojistas em MG e no Norte do Rio. Antes, nós éramos uma distribuidora apenas da marca Vorani (https://www.voranicosmeticos.com.br/). Por esse motivo, utilizávamos uma logo feita pelo marketing deles, nas cores deles, para que as duas logos sempre andassem casadas. Hoje, ampliamos o nosso mix e distribuímos também os produtos da Mirtex ( https://www.mirtex.com.br/) e da henna Sol de Jade. Ou seja, hoje somos efetivamente uma distribuidora de Cosméticos em geral, atendendo os michos de cabelo, pele, maquiagem e unhas. Dessa maneira, criamos uma nova logo, para representar a Distribuidora. "

```html
<!DOCTYPE html>
<html lang="pt-BR">
<head>
<meta charset="utf-8">
<title>Lunara – Envelopes</title>
<link rel="stylesheet" href="https://fonts.googleapis.com/css2?family=Montserrat:wght@300;400;600&display=swap">
<style>
  :root{
    --bg:#2b2c2f;
    --navy:#131c2b;
    --navy-deep:#0b111c;
    --navy-light:#243247;
    --paper:#ffffff;
    --paper-shade:#eceef1;
    --gold:#c9a25a;
    --gold-light:#e4c98f;
    --ink:#2a3140;
    --muted:#6b7280;
  }
  *{box-sizing:border-box;margin:0;padding:0}
  html,body{width:1200px;height:1200px;overflow:hidden;background:var(--bg);font-family:"Montserrat",sans-serif}
  .stage{position:relative;width:1200px;height:1200px}
  .envelope{position:absolute;top:209px;width:545px;height:787px;overflow:hidden}
  .envelope--front{left:36px;background:linear-gradient(160deg,var(--paper) 40%,var(--paper-shade));}
  .envelope--back{left:619px;background:radial-gradient(ellipse at 40% 45%,var(--navy-light),var(--navy) 55%,var(--navy-deep));}
  .envelope svg.decor{position:absolute;inset:0;width:100%;height:100%}
  .brand{position:absolute;left:0;right:0;display:flex;justify-content:center;align-items:center;gap:10px}
  .brand__dot{width:30px;height:30px;border-radius:50%;border:2px solid var(--gold);flex:none}
  .brand__text{display:flex;flex-direction:column}
  .brand__name{font-weight:300;letter-spacing:.12em;line-height:1}
  .brand__tag{font-weight:600;letter-spacing:.14em;text-transform:uppercase;margin-top:4px}
  .envelope--front .brand{top:862px;top:862px}
  .envelope--front .brand{top:653px}
  .envelope--front .brand__name{color:var(--ink);font-size:30px}
  .envelope--front .brand__tag{color:var(--ink);font-size:6.5px}
  .envelope--back .brand{top:360px;gap:14px}
  .envelope--back .brand__dot{width:44px;height:44px}
  .envelope--back .brand__name{color:#fff;font-size:40px}
  .envelope--back .brand__tag{color:#fff;font-size:8.5px}
  .contact{position:absolute;left:22px;right:22px;top:734px;display:flex;justify-content:space-between;align-items:center;font-size:8px;color:var(--muted)}
  .contact__item{display:flex;align-items:center;gap:6px;line-height:1.35}
  .contact__icon{width:14px;height:14px;border-radius:50%;background:var(--ink);display:flex;align-items:center;justify-content:center;flex:none}
  .contact__icon svg{width:8px;height:8px}
  .gold-rule{position:absolute;left:0;right:0;top:745px;height:2px;background:linear-gradient(90deg,transparent,var(--gold-light),var(--gold),transparent)}
</style>
</head>
<body>
<main class="stage">
  <section class="envelope envelope--front" aria-label="Envelope frente">
    <svg class="decor" viewBox="0 0 545 787" aria-hidden="true">
      <circle cx="290" cy="380" r="250" fill="none" stroke="#e9ebee" stroke-width="28"/>
      <path d="M0 0 H545 V56 Q545 96 505 96 H40 Q0 96 0 56 Z" fill="var(--navy)"/>
      <path d="M20 96 Q272 70 525 96" fill="none" stroke="#2f3d55" stroke-width="2"/>
    </svg>
    <div class="brand">
      <span class="brand__dot"></span>
      <div class="brand__text">
        <span class="brand__name">LUNARA</span>
        <span class="brand__tag">Distribuidora de cosméticos</span>
      </div>
    </div>
    <div class="contact">
      <div class="contact__item">
        <span class="contact__icon"><svg viewBox="0 0 10 10"><path d="M5 1a3 3 0 0 1 3 3c0 2-3 5-3 5S2 6 2 4a3 3 0 0 1 3-3z" fill="#fff"/></svg></span>
        <span>Av. das Acácias, 415<br>Centro - Muriaé - MG - CEP 36880-000</span>
      </div>
      <div class="contact__item">
        <span class="contact__icon"><svg viewBox="0 0 10 10"><path d="M2.5 1l1.5 2-1 1c.5 1.2 1.3 2 2.5 2.5l1-1 2 1.5-1 1.5C5 8.5 1.5 5 1 2.5z" fill="#fff"/></svg></span>
        <span>(32) 3104 2280</span>
      </div>
      <div class="contact__item">
        <span class="contact__icon"><svg viewBox="0 0 10 10"><rect x="1.5" y="2.5" width="7" height="5" fill="none" stroke="#fff"/><path d="M1.5 2.5 5 5.5 8.5 2.5" fill="none" stroke="#fff"/></svg></span>
        <span>contato@lunaracosmeticos.com.br</span>
      </div>
    </div>
  </section>

  <section class="envelope envelope--back" aria-label="Envelope verso">
    <svg class="decor" viewBox="0 0 545 787" aria-hidden="true">
      <circle cx="250" cy="390" r="300" fill="none" stroke="#2c3b52" stroke-width="10" opacity=".6"/>
      <circle cx="250" cy="390" r="330" fill="none" stroke="#1d2839" stroke-width="4" opacity=".7"/>
    </svg>
    <div class="brand">
      <span class="brand__dot"></span>
      <div class="brand__text">
        <span class="brand__name">LUNARA</span>
        <span class="brand__tag">Distribuidora de cosméticos</span>
      </div>
    </div>
    <div class="gold-rule"></div>
  </section>
</main>
</body>
</html>
```